Redesign Login page

I want to redesign my login page to bring my 2 products closer together. I am only looking to redesign one login page, not 2.

For the logo, please make it solid and it can be black or white if helpful. I can also fine tune the logo if you get it close.

Coding

Coded - Design and coding required

Number of Pages Required

1 page

```html
<!DOCTYPE html>
<html lang="en">
<head>
<meta charset="UTF-8">
<title>Norvik – Sign In</title>
<link rel="stylesheet" href="https://fonts.googleapis.com/css2?family=Inter:wght@400;500;600;700&family=Lato:wght@700&display=swap">
<style>
  :root {
    --ink: #111111;
    --muted: #7a7a7a;
    --title: #3f6e66;
    --primary: #456460;
    --tab-bg: #f0f0f0;
    --line: #d9d9d9;
    --success: #1fae8c;
    --panel-light: #e8f6f3;
    --panel-mid: #9fd9cf;
    --panel-deep: #54b8a8;
    --white: #ffffff;
  }
  * { box-sizing: border-box; margin: 0; padding: 0; }
  html, body { width: 1200px; height: 794px; overflow: hidden; background: var(--white); }
  body { font-family: "Inter", sans-serif; color: var(--ink); position: relative; }

  .auth { position: absolute; left: 0; top: 0; width: 600px; height: 794px; }

  .brand {
    position: absolute; left: 0; width: 600px; top: 50px;
    text-align: center; font-size: 32px; font-weight: 700; letter-spacing: -0.5px; color: var(--ink);
  }

  .title {
    position: absolute; left: 0; width: 600px; top: 197px; text-align: center;
    font-family: "Lato", sans-serif; font-weight: 700; font-size: 31px; color: var(--title); letter-spacing: -0.3px;
  }
  .subtitle {
    position: absolute; left: 0; width: 600px; top: 242px; text-align: center;
    font-size: 14px; color: var(--muted);
  }

  .tabs {
    position: absolute; left: 154px; top: 281px; width: 291px; height: 44px;
    background: var(--tab-bg); border-radius: 8px; display: flex; padding: 3px;
  }
  .tab { flex: 1; display: flex; align-items: center; justify-content: center; font-size: 14.5px; color: var(--muted); border-radius: 6px; letter-spacing: 0.3px; }
  .tab--active { background: var(--white); color: var(--ink); font-weight: 500; }

  .field {
    position: absolute; left: 154px; top: 345px; width: 291px; height: 53px;
    border: 1px solid var(--line); border-radius: 8px;
  }
  .field__icon { position: absolute; left: 18px; top: 18px; }
  .field__divider { position: absolute; left: 53px; top: 12px; width: 1px; height: 28px; background: var(--line); }
  .field__label { position: absolute; left: 71px; top: 8px; font-size: 12px; color: #444; letter-spacing: 0.2px; }
  .field__value { position: absolute; left: 71px; top: 24px; font-size: 15px; color: var(--ink); }
  .field__check { position: absolute; right: 16px; top: 17px; }

  .btn-primary {
    position: absolute; left: 154px; top: 418px; width: 291px; height: 48px;
    background: var(--primary); border-radius: 8px; color: var(--white);
    display: flex; align-items: center; justify-content: center;
    font-size: 14.5px; font-weight: 700; letter-spacing: 0.6px;
  }

  .divider {
    position: absolute; left: 154px; top: 492px; width: 291px;
    display: flex; align-items: center; gap: 8px; font-size: 12px; color: var(--muted);
  }
  .divider::before, .divider::after { content: ""; flex: 1; height: 1px; background: #cfcfcf; }

  .socials { position: absolute; left: 212px; top: 529px; display: flex; gap: 20px; }
  .social { width: 45px; height: 45px; border-radius: 50%; }
  .social--one { border: 1.5px solid var(--line); background: var(--white); }
  .social--two { background: var(--ink); }
  .social--three { background: var(--primary); }

  .legal {
    position: absolute; left: 40px; width: 520px; top: 709px; text-align: center;
    font-size: 13.5px; line-height: 19.5px; color: var(--muted);
  }

  .visual {
    position: absolute; left: 600px; top: 0; width: 600px; height: 794px;
    background: radial-gradient(circle at 50% 45%, var(--panel-light) 0%, var(--panel-mid) 45%, var(--panel-deep) 100%);
  }
</style>
</head>
<body>
  <main class="auth">
    <div class="brand">Norvik</div>

    <h1 class="title">Welcome Back</h1>
    <p class="subtitle">Welcome back, please enter your details</p>

    <div class="tabs">
      <div class="tab tab--active">Sign In</div>
      <div class="tab">Sign Up</div>
    </div>

    <div class="field">
      <svg class="field__icon" width="18" height="15" viewBox="0 0 18 15" fill="none" stroke="#111" stroke-width="1.6">
        <rect x="1" y="1" width="16" height="13" rx="1"/>
        <path d="M1.5 2 L9 8 L16.5 2"/>
      </svg>
      <span class="field__divider"></span>
      <span class="field__label">Email Address</span>
      <span class="field__value">jordan.lee@example.net</span>
      <svg class="field__check" width="17" height="17" viewBox="0 0 17 17">
        <circle cx="8.5" cy="8.5" r="8.5" fill="var(--success)"/>
        <path d="M4.8 8.7 L7.4 11.2 L12.2 6.2" fill="none" stroke="#fff" stroke-width="1.7" stroke-linecap="round" stroke-linejoin="round"/>
      </svg>
    </div>

    <div class="btn-primary">Continue</div>

    <div class="divider">Or Connect With</div>

    <div class="socials">
      <span class="social social--one" aria-label="Continue with provider one"></span>
      <span class="social social--two" aria-label="Continue with provider two"></span>
      <span class="social social--three" aria-label="Continue with provider three"></span>
    </div>

    <p class="legal">Lorem ipsum dolor sit amet, consectetur adipiscing elit, sed do eiusmod tempor incididunt ut labore et dolore magna aliqua. Ut enim ad minim veniam, quis nostrud exercitation ullamco laboris nisi ut aliquip ex</p>
  </main>

  <aside class="visual" role="img" aria-label="Laptop with a filing cabinet drawer of binders emerging from its screen, on a teal background"></aside>
</body>
</html>
```